New Alcoholic Spiked Seltzer Line

We need a can design for a line of low calorie alcoholic seltzer. This product is a sparkling water and vodka drink with no sugar added in a slim 12 oz can.

This is a lighter, healthier, alternative to the sugary ready-to-drinks on the market. The product contains only 3 ingredients: Vodka, Water and Natural Flavors. It has only 100 calories but still has 5% alcohol, so you don't need to sacrifice alcohol to cut calories.

This product also does not contain any preservatives.

We want this design to communicate the following objectives to the consumer and in this order:

1. Appetizing product
2.Low calorie
3.Communicate the type of beverage (Spiked Seltzer)

The brand name of the product is VELKA.

The flavor of the product needed to be used for the design is Mango-Orange.

Comparable products are:

www.brisavelfizz.example/
https://www.tarnowbubble.example
https://quellrind.example/

The designs should not infringe or copy the creative directions of the products mentionned above. They are only given so that you can better understand the type of product we are developing.

Target Market(s)

Young Professional women between the ages of 25 and 44

Industry/Entity Type

Product

Colors

Designer to choose colors to be used in the design.

Requirements
Must have
• Design extendibility, meaning it can be adapted for other flavors.
• This is a new category in the market we are targeting, so consumers must easily be able to identify what type of product this is.

```html
<!DOCTYPE html>
<html lang="en">
<head>
<meta charset="utf-8">
<title>VELKA Mango Orange Spiked Seltzer – Can Label</title>
<link rel="stylesheet" href="https://fonts.googleapis.com/css2?family=Roboto+Condensed:wght@400;500&display=swap">
<style>
  :root {
    --backdrop-light: #f4f6f7;
    --backdrop-dark: #dde2e5;
    --label-black: #1f1f20;
    --label-charcoal: #363638;
    --fruit-yellow: #f7c21a;
    --fruit-orange: #f0a21c;
    --fruit-red: #d9622a;
    --flavor-gold: #f3b51c;
    --logo-white: #ffffff;
  }
  * { margin: 0; padding: 0; box-sizing: border-box; }
  html, body {
    width: 1200px;
    height: 1200px;
    overflow: hidden;
  }
  body {
    background: radial-gradient(ellipse at 50% 40%, var(--backdrop-light) 0%, var(--backdrop-dark) 100%);
    font-family: "Roboto Condensed", "Arial Narrow", sans-serif;
  }
  .can-label {
    position: absolute;
    left: 420px;
    top: 150px;
    width: 360px;
    height: 920px;
    overflow: hidden;
  }
  .label-art {
    position: absolute;
    inset: 0;
    width: 100%;
    height: 100%;
  }
  .brand-name {
    font-family: "Roboto Condensed", "Arial Narrow", sans-serif;
    font-size: 200px;
    font-weight: 400;
    fill: var(--logo-white);
  }
  .product-info {
    position: absolute;
    left: 0;
    right: 0;
    top: 838px;
    text-align: center;
    line-height: 1.2;
  }
  .flavor-name {
    display: block;
    font-size: 21px;
    font-weight: 500;
    color: var(--flavor-gold);
  }
  .product-type {
    display: block;
    font-size: 22px;
    font-weight: 500;
    color: var(--logo-white);
  }
</style>
</head>
<body>
  <main class="can-label">
    <svg class="label-art" viewBox="0 0 360 920" xmlns="http://www.w3.org/2000/svg">
      <defs>
        <linearGradient id="panelShade" x1="0" y1="0" x2="1" y2="1">
          <stop offset="0" stop-color="var(--label-charcoal)"/>
          <stop offset="1" stop-color="var(--label-black)"/>
        </linearGradient>
        <linearGradient id="fruitTones" x1="0" y1="0" x2="1" y2="1">
          <stop offset="0" stop-color="var(--fruit-orange)"/>
          <stop offset="0.45" stop-color="var(--fruit-yellow)"/>
          <stop offset="0.7" stop-color="var(--fruit-red)"/>
          <stop offset="1" stop-color="var(--fruit-yellow)"/>
        </linearGradient>
      </defs>
      <rect class="dark-panel" x="0" y="0" width="360" height="920" fill="url(#panelShade)"/>
      <path class="fruit-area" role="img" aria-label="Photo of a halved orange and diced mango"
            d="M0 0 H360 V102 Q150 110 0 280 Z" fill="url(#fruitTones)"/>
      <text class="brand-name" transform="translate(184 495) rotate(90)" text-anchor="middle"
            dy="0.355em" textLength="640" lengthAdjust="spacing">VELKA</text>
    </svg>
    <p class="product-info">
      <span class="flavor-name">MANGO ORANGE</span>
      <span class="product-type">SPIKED SELTZER</span>
    </p>
  </main>
</body>
</html>
```